Calmwell Learning - Wordpress Design Project

*IMPORTANT UPDATE*

The new Wordpress theme will be based on the Corvale Institute website templates (attached: http://www.pitchloom.com.au/file.aspx?fileLocation=storage_url/brief_uploads/74826_universitystandardwebtemplate_320_brief135807.zip).

Please do not take the design of the old Wordpress theme into account. The logo, icons, graphics from the old Wordpress theme are not to be used in your design.

1. Project overview

We need a customised wordpress theme and need to update the existing website www.calmwelllearning.edu.au using the Corvale Institute branding components such as logo, colours, text sizes, fonts, table styles etc.

2. Project aim

We would like the new website to make more online marketing sense. That is, we would like to increase student enrolment by improving the information on the website. Therefore, the new website needs to quickly communicate to the first time audience that: (1) this is a website from Corvale Institute, (2) this web site offers a self-paced multimedia e-learning course in Anxiety Disorders, (3) this course is accredited by professional organisations and supported by the Australian Government, (4) the course is lectured by 21 experts, (5) the price is AU$400 for 6 month access and AU$200 for extension for another 6 months, (6) users can sign up for the course online and get immediate access, (7) the benefits of learning the course, (8) the learning outcome, and (9) users can access to a lot of information for free on the website (this is to be done in two ways - the new website will have a blog, and it will offer a free ebook which the users can get via e-mail - they need to supply their first name and e-mail address).

3. Branding examples

The following are examples of different websites that apply the brand styles:

http://openhall.corvale.edu.au

http://big-questions.corvale.edu.au

http://mba.corvale.edu.au

http://inkbranch.corvale.edu.au

http://www.library.cvin.edu.au

http://blogs.cvin.edu.au/campusdays

http://corvale.edu.au/alumni/kit

4. Information to be used for the design of the new website:

(1) Information (e.g. text) from existing website: http://www.calmwelllearning.edu.au

(2) Information from course outline web pages:
http://pdl.corvale.edu.au/course/clmw

(3) Program flyer:
http://www.calmwelllearning.edu.au/info/wp-content/uploads/2012/03/CLHP-Flyer-3-pages.pdf

5. Things to have on the home page

The following components are something that I would suggest be included in the home page, but I would like to leave the freedom for designers to create:

(1) Menu

(2) E-Learning Portal Login form (pointing to http://www.calmwelllearning.edu.au/e-learning)

(3) Sign up button/link

(4) Information about accreditation

(5) Latest posts from the blog

(6) Free e-book opt in form - "Nine Ways Through Restless Worry" (we will use MailChimp to deliver the e-book to the e-mail address that audience submits)

(7) Information about lecturers

(8) Our Facebook Page, Twitter and Linked Group

6. Home page layout

I would like to see different layout styles and compare. The two extremes of the spectrum would be either something like this: http://www.clinicpath.com.au/ (very clean), or something more crowded like some of the examples above.

7. Attachments

Our University has some templates (including style sheets) for web designers to use. I'm also attaching a brand guideline for designer's information. I have some screenshots of the e-learning program that may be used in the design.
Updates

Dear all,

Thanks for your participation. I'm sending you some important updates:

The Corvale Institute website templates (attached: http://www.pitchloom.com.au/file.aspx?fileLocation=storage_url/brief_uploads/74826_universitystandardwebtemplate_320_brief135807.zip) should be used as a starting point for your design.

The new Wordpress theme should carry a strong Corvale Institute brand, utilising the "Grid of Ideas" framework. Please refer to Page 43, 49, 52, and 53 of the Corvale Institute brand identity document: http://www.pitchloom.com/file.aspx?fileLocation=storage_url/brief_uploads/74826_corvale_institute_brand_identity_brief131935.pdf

You may get inspired from the following websites:

http://mba.corvale.edu.au

http://kindle.corvale.edu.au/

Thanks a lot!

Further to the update yesterday, I just posted one more file containing some examples of possible heading design.

They are all examples of the "Grid of Ideas" design style (square matrix with logo). Our new website will need to apply this style as well.

Please download this file:

Please remember: when a prospect customer descides to sign up, they will have to go to this page http://pdl.cvin.edu.au/course/CLMW to process credit card payment. Therefore, the Wordpress design should connect to that payment page naturaly, without making people think they are going somewhere else.

Reason: Designers, thanks for your interest in this project. As per request, I have extended the deadline due to Christmas and New Year holiday. Happy New Year to all!

Target Market(s)

Target audiences are psychiatrists, psychologists, nurses, social workers, relationship therapists, teachers, counsellours etc. from all around the world

Industry/Entity Type

Marketing

Requirements
Must have
• Corvale Institute logo along with the blue square should be used.
Should not have
• Please do not take the design of the old Wordpress theme (http://www.CalmwellLearning.edu.au) into account. The logo, icons, graphics from the old Wordpress theme are not to be used in your design.

```html
<!DOCTYPE html>
<html lang="en">
<head>
<meta charset="utf-8">
<title>Calmwell Learning for Health Professionals</title>
<link href="https://fonts.googleapis.com/css2?family=Arimo:wght@400;700&display=swap" rel="stylesheet">
<style>
:root{
  --navy:#1f4675;
  --navy-dark:#173a63;
  --brand-red:#d8202f;
  --heading-red:#d7132a;
  --amber:#f9b01e;
  --amber-light:#fcc233;
  --link-blue:#1c5fa8;
  --text:#4a4a4a;
  --panel:#f6f6f6;
  --sidebar:#6b6b6b;
  --sidebar-dark:#5c5c5c;
  --footer:#f1f1f1;
  --btn-dark:#3b3b3b;
}
*{box-sizing:border-box;margin:0;padding:0}
html,body{width:890px;height:1200px;overflow:hidden;background:#fff}
body{font-family:"Arimo",Arial,sans-serif;color:var(--text);font-size:10px;position:relative}
.abs{position:absolute}
a{color:inherit;text-decoration:none}

/* header */
.masthead{left:66px;top:0;width:756px;height:118px;background:var(--navy)}
.brand{left:38px;top:3px;width:186px;height:71px;background:var(--brand-red);display:flex;align-items:center;gap:9px;padding-left:12px}
.brand-square{width:28px;height:28px;background:#fff}
.brand-name{color:#fff;font-size:17px;font-weight:400;letter-spacing:.5px;line-height:1.1}
.site-title{right:80px;top:30px;color:#fff;font-size:13px;letter-spacing:.3px}
.search{left:650px;top:75px;width:159px;height:25px;background:#fff;border:1px solid #cfd6de;font-size:8px;font-style:italic;color:#999;padding:8px 0 0 11px}
.search svg{position:absolute;right:8px;top:8px}
.utility-nav{left:89px;top:91px;color:#fff;font-size:9.5px;display:flex;gap:0}
.utility-nav span{margin-right:21px}
.utility-caret{left:97px;top:112px;width:0;height:0;border-left:5px solid transparent;border-right:5px solid transparent;border-bottom:6px solid var(--amber)}
.main-nav{left:66px;top:118px;width:756px;height:28px;background:var(--amber);display:flex;border-bottom:1px solid #e49a12}
.main-nav a{font-size:9px;color:#333;display:flex;align-items:center;justify-content:center;border-right:1px solid #e6a215}
.main-nav .home{background:#f7a514}

/* hero */
.hero-copy{left:66px;top:161px;width:318px;height:240px;background:var(--navy);padding:17px 14px 0 22px;color:#fff}
.hero-copy h1{color:var(--amber-light);font-weight:400;font-size:13.5px;line-height:26px;white-space:nowrap}
.hero-copy p{font-size:9.5px;line-height:14px;text-align:justify;margin-top:10px;margin-left:2px;margin-right:8px}
.hero-btn{display:inline-flex;align-items:center;gap:8px;background:var(--amber-light);color:#1b1b1b;font-size:9.5px;padding:7px 8px;margin-top:8px;margin-left:2px}
.hero-photo-a{left:384px;top:161px;width:254px;height:197px;background:linear-gradient(135deg,#e8e8e8,#9a9a9a 60%,#c9c9c9)}
.hero-fill{left:384px;top:358px;width:254px;height:43px;background:var(--navy)}
.hero-photo-b{left:638px;top:167px;width:177px;height:280px;background:linear-gradient(180deg,#efeae6,#c49b83 45%,#d9d1ca)}
.login-bar{left:66px;top:401px;width:756px;height:55px;background:var(--amber-light);display:flex;align-items:center;padding-left:22px}
.login-bar .title{font-size:14px;color:#2a2a2a;margin:0 13px 0 8px}
.field{height:22px;background:#fff;border:1px solid #e8d08a;font-size:8.5px;font-style:italic;color:#aaa;padding:6px 14px;margin-right:9px}
.login-btn{background:var(--navy);color:#fff;font-size:11px;padding:4px 10px;border:1px solid #0f2c50}

/* feature columns */
.features{left:66px;top:456px;width:756px;height:196px;background:var(--panel);display:flex;padding-top:42px}
.feature{width:252px;padding:0 10px;border-right:1px solid #e4e4e4}
.feature:last-child{border:0}
.feature h2{color:var(--heading-red);font-size:14px;font-weight:400;padding-bottom:9px;border-bottom:1px solid #e2e2e2}
.feature p{font-size:9px;line-height:17px;text-align:justify;margin-top:14px}
.btn-dark{display:inline-block;background:var(--btn-dark);color:#fff;font-size:9px;padding:5px 9px;border-bottom:2px solid #999}
.feature .btn-dark{margin-top:16px}

/* accreditation */
.accreditation{left:68px;top:686px;width:497px;padding-bottom:15px;border-bottom:1px solid #e4e4e4}
.section-title{color:var(--heading-red);font-size:14px;font-weight:400}
.accreditation p{font-size:9px;line-height:17px;margin-top:10px}
.accreditation .btn-dark{margin-top:11px}

/* blog */
.blog-head{left:67px;top:848px;width:496px}
.blog-arrows{right:0;top:0;display:flex;gap:1px}
.blog-card{left:68px;top:876px;width:494px;height:134px;background:#f6f6f6;border:1px solid #e6e6e6;padding:8px}
.blog-photo{left:8px;top:8px;width:142px;height:117px;background:linear-gradient(135deg,#c7a58a,#7d96ac 60%,#d9dde3)}
.blog-body{left:160px;top:6px;width:326px}
.blog-body h3{color:var(--link-blue);font-size:11.5px;font-weight:400}
.blog-body p{font-size:9px;line-height:17px;text-align:justify;margin-top:7px}
.blog-meta{font-size:8px;margin-top:10px;display:flex;align-items:center;gap:5px}
.blog-meta .more{color:var(--link-blue);text-decoration:underline;font-size:9px}
.pill{border:1px solid #ccc;background:#fff;font-size:7px;padding:1px 3px;color:#335}

/* ebook */
.ebook{left:601px;top:689px;width:221px;height:287px;background:var(--sidebar);border:2px solid #555}
.ebook-top{height:82px;background:linear-gradient(#7a7a7a,#686868);border-bottom:1px solid #4d4d4d;position:relative}
.ebook-icon{left:20px;top:22px;width:38px;height:42px;background:#e4e4e4;border:1px solid #bbb}
.ebook-title{left:77px;top:14px;color:#fff;font-size:17px}
.signup{left:84px;top:39px;width:104px;height:25px;background:#f4f4f4;border:1px solid #bbb;color:#333;font-size:9.5px;display:flex;align-items:center;justify-content:center;gap:6px}
.ebook-form{padding:15px 13px 0 12px;color:#fff;font-size:8.5px}
.ebook-row{display:flex;align-items:center;margin-top:11px}
.ebook-row label{width:51px;font-size:9.5px}
.ebook-row span{width:143px;height:24px;background:#fff;border:1px solid #ccc}
.ebook-actions{display:flex;justify-content:flex-end;align-items:center;gap:20px;margin-top:20px}
.ebook-actions a{text-decoration:underline;font-size:8px}
.submit{background:#ddd;color:#333;font-size:9.5px;padding:5px 9px}
.payments{left:614px;top:993px;display:flex;align-items:center;gap:7px;color:var(--link-blue);font-size:10.5px}
.card{width:22px;height:14px;border-radius:2px}

/* partners */
.partners{left:66px;top:1036px;width:756px;height:80px;border-top:1px solid #e6e6e6;display:flex;align-items:center;justify-content:space-between;padding:0 2px}
.partner{display:flex;align-items:center;gap:5px;color:#8a8a8a;font-size:9px;line-height:11px}
.partner i{display:block;width:18px;height:18px;border-radius:50%;background:#a8a8a8}

/* footer */
.footer{left:0;top:1120px;width:890px;height:80px;background:var(--footer)}
.footer-links{left:67px;top:15px;font-size:9px;color:#444;word-spacing:2px}
.copyright{left:67px;top:38px;font-size:9px;color:#444}
.social{left:726px;top:22px;display:flex;gap:7px}
.social i{display:block;width:19px;height:19px;border-radius:50%;background:#9a9a9a}
</style>
</head>
<body>

<header>
  <div class="abs masthead"></div>
  <a class="abs brand" href="#"><span class="brand-square"></span><span class="brand-name">CORVALE<br>INSTITUTE</span></a>
  <div class="abs site-title">CALMWELL LEARNING FOR HEALTH PROFESSIONALS (CLHP)</div>
  <div class="abs search">Search
    <svg width="8" height="8" viewBox="0 0 8 8"><circle cx="3.2" cy="3.2" r="2.4" fill="none" stroke="#999" stroke-width="1"/><line x1="5" y1="5" x2="7.5" y2="7.5" stroke="#999"/></svg>
  </div>
  <nav class="abs utility-nav">
    <span>CLHP</span><span>|</span><span>UNIVERSITY HOME</span><span>|</span><span>CONTACT US</span><span>|</span><span>SITEMAP</span>
  </nav>
  <div class="abs utility-caret"></div>
  <nav class="abs main-nav">
    <a class="home" style="width:71px" href="#">HOME</a>
    <a style="width:90px" href="#">ABOUT US</a>
    <a style="width:80px" href="#">COURSE</a>
    <a style="width:100px" href="#">RESOURCES</a>
    <a style="width:98px" href="#">CONTACT US</a>
    <a style="width:71px" href="#">HELP</a>
  </nav>
</header>

<section>
  <div class="abs hero-copy">
    <h1>CLHP :Online Continuing Professional<br>Development Course in Anxiety Disorders</h1>
    <p>Spend 24 online learning hours with us, and you will be equipped with comprehensive and specialised knowledge that enables you to effectively communicate with and provide helpful advice to people with anxiety disorders.</p>
    <p>Sed ut perspiciatis unde omnis iste natus error sit voluptatem accusantium doloremque laudantium, totam rem aperiam, eaque ipsa quae ab illo inventore veritatis.</p>
    <a class="hero-btn" href="#">View More Details
      <svg width="11" height="11" viewBox="0 0 11 11"><circle cx="5.5" cy="5.5" r="5.5" fill="#1b1b1b"/><path d="M4.3 3l2.6 2.5-2.6 2.5" fill="none" stroke="#fcc233" stroke-width="1.4"/></svg>
    </a>
  </div>
  <div class="abs hero-photo-a" role="img" aria-label="Black and white photo of a worried man holding his forehead"></div>
  <div class="abs hero-fill"></div>
  <div class="abs login-bar">
    <svg width="20" height="26" viewBox="0 0 20 26"><path d="M5 12V8a5 5 0 0 1 10 0v4" fill="none" stroke="#777" stroke-width="2.4"/><rect x="2" y="11" width="16" height="14" rx="2" fill="#9a8a6a"/></svg>
    <span class="title">E-Learning Portal Login</span>
    <span class="field" style="width:132px">Username</span>
    <span class="field" style="width:132px">Password</span>
    <span class="login-btn">Log in</span>
  </div>
  <div class="abs hero-photo-b" role="img" aria-label="Photo of a smiling student holding a folder"></div>
</section>

<section class="abs features">
  <div class="feature">
    <h2>THE CLHP COURSE</h2>
    <p>The Calmwell Learning for Health Professionals (CLHP) is a self-paced online course collaboratively designed by 21 academics, clinicians and educators ...</p>
    <a class="btn-dark" href="#">View more</a>
  </div>
  <div class="feature">
    <h2>LECTURERS</h2>
    <p>The Calmwell Learning for Health Professionals (CLHP) is a self-paced online course collaboratively designed by 21 academics, clinicians and educators ...</p>
    <a class="btn-dark" href="#">View more</a>
  </div>
  <div class="feature">
    <h2>BENEFITS TO PARTICIPANTS</h2>
    <p>The Calmwell Learning for Health Professionals (CLHP) is a self-paced online course collaboratively designed by 21 academics, clinicians and educators ...</p>
    <a class="btn-dark" href="#">View more</a>
  </div>
</section>

<section class="abs accreditation">
  <h2 class="section-title">ABOUT ACCREDITATION</h2>
  <p>CPD accreditation for CLHP has been awarded with a number of specialist colleges and professional associations in the health care field. Those participants who successfully complete the course will be issued a Certificate of Achievement or a Certificate of Participation depending on their scores in the final examination. With either certificate, participants may be able to claim up to 24 CPD hours.</p>
  <a class="btn-dark" href="#">View more</a>
</section>

<section>
  <div class="abs blog-head">
    <h2 class="section-title">BLOG</h2>
    <div class="abs blog-arrows">
      <svg width="21" height="13" viewBox="0 0 21 13"><rect width="10" height="13" rx="6" fill="#555"/><rect x="11" width="10" height="13" rx="6" fill="#555"/><path d="M6.5 3.5L3.5 6.5l3 3M14.5 3.5l3 3-3 3" fill="none" stroke="#fff" stroke-width="1.4"/></svg>
    </div>
  </div>
  <article class="abs blog-card">
    <div class="abs blog-photo" role="img" aria-label="Photo of students studying together at a desk"></div>
    <div class="abs blog-body">
      <h3>Suspendisse potenti</h3>
      <p>Curabitur tortor tellus, volutpat eu lacinia eu, viverra ac velit. Morbi feugiat convallis feugiat. Vivamus ullamcorper tempus ipsum a ornare. Cras facilisis urna sit amet tortor pellentesque nec hendrerit tellus volutpat....</p>
      <div class="blog-meta">Dec 14, 2012 &nbsp;| &nbsp;Post by : Mara Lindqvist &nbsp;| <a class="more" href="#">View more</a> | <span class="pill">Like</span><span class="pill">3k</span><span class="pill">Share</span><span class="pill">316</span></div>
    </div>
  </article>
</section>

<aside class="abs ebook">
  <div class="ebook-top">
    <div class="abs ebook-icon" role="img" aria-label="Illustration of a notepad and pen"></div>
    <div class="abs ebook-title">FREE E-BOOK</div>
    <a class="abs signup" href="#">
      <svg width="10" height="9" viewBox="0 0 10 9"><circle cx="5" cy="2.5" r="2.3" fill="#444"/><path d="M0.5 9c0-3 2-4.2 4.5-4.2S9.5 6 9.5 9z" fill="#444"/></svg>SIGN UP NOW</a>
  </div>
  <div class="ebook-form">
    <div>Nine Ways Through Restless Worry</div>
    <div class="ebook-row" style="margin-top:15px"><label>Name :</label><span></span></div>
    <div class="ebook-row"><label>E-mail :</label><span></span></div>
    <div class="ebook-row"><label>Phone :</label><span></span></div>
    <div class="ebook-actions"><a href="#">Forgot password</a><span class="submit">SUBMIT</span></div>
  </div>
</aside>
<div class="abs payments">Payments : <span class="card" style="background:#c9d6e6;margin-left:6px"></span><span class="card" style="background:#d9e0ee"></span><span class="card" style="background:#efe6c8"></span><span class="card" style="background:#cfe4c6"></span></div>

<section class="abs partners">
  <div class="partner"><i></i>Harbourline College<br>of Care Nurses</div>
  <div class="partner"><i></i>Outback Fellowship<br>of Rural Medicine</div>
  <div class="partner"><i></i>National Council<br>for Health Research</div>
  <div class="partner"><i></i>Everyday<br>Therapy Guild</div>
  <div class="partner"><i></i>Tasman College<br>of Psychiatrists</div>
</section>

<footer class="abs footer">
  <div class="abs footer-links">Home &nbsp;| &nbsp;About us &nbsp;| &nbsp;Course &nbsp;| &nbsp;Resources &nbsp;| &nbsp;Contact us &nbsp;| &nbsp;Help &nbsp;| &nbsp;Sign up &nbsp;| &nbsp;Login &nbsp;| &nbsp;Terms and conditions &nbsp;| &nbsp;Privacy Policy</div>
  <div class="abs copyright">Copyright &nbsp;© &nbsp;2012 &nbsp; www.calmwelllearning.edu.au &nbsp; All rights reserved.</div>
  <div class="abs social"><i></i><i></i><i></i><i></i></div>
</footer>

</body>
</html>
```